Larkspur Vision Optometrists

News paper advertisement (150mm H x 110mm W).
Eye testing (Salubra covered).
Prescription glasses,sunglasses & contact lenses.
All major health funds accepted.
Phone: 95550132 for an appointment at our Claremont practice
or Phone: 95550478 for an appointment at our Subiaco practice.
Please disregard "Good health for less" slogan.
We are an independent Optometry practice providing major fashion brands in both Optical frames & sunglasses.
Keep it simple and / or entertaining.
Use of company logo not critical, only discretionary.
Use as much or as little of this information as you wish.

```html
<!DOCTYPE html>
<html lang="en">
<head>
<meta charset="utf-8">
<title>Larkspur Vision Optometrists – Newspaper Advertisement</title>
<link href="https://fonts.googleapis.com/css2?family=Questrial&family=Montserrat:wght@700&family=Arimo&display=swap" rel="stylesheet">
<style>
  :root {
    --stage: #6b6b6b;
    --paper: #ffffff;
    --ink: #3d3d3d;
    --accent-red: #e8141b;
    --brand-blue: #1637c9;
    --hair-dark: #1f150f;
    --hair-mid: #4a3225;
    --skin-deep: #c99877;
    --skin-mid: #e2bca2;
    --skin-light: #f5e3d6;
    --photo-grey-1: #e4e4e4;
    --photo-grey-2: #fafafa;
  }
  * { margin: 0; padding: 0; box-sizing: border-box; }
  html, body { width: 900px; height: 1200px; overflow: hidden; background: var(--stage); }
  .canvas { position: relative; width: 900px; height: 1200px; }
  .advert {
    position: absolute; left: 125px; top: 157px; width: 650px; height: 886px;
    background: var(--paper); overflow: hidden;
    box-shadow: 0 18px 40px rgba(0,0,0,0.35);
  }
  .portrait-colour {
    position: absolute; left: 0; top: 0; width: 278px; height: 886px;
    background:
      radial-gradient(ellipse 230px 330px at 100% 62%, var(--skin-light) 0%, var(--skin-mid) 45%, rgba(226,188,162,0) 100%),
      radial-gradient(ellipse 260px 260px at 85% 95%, var(--skin-mid) 0%, rgba(245,227,214,0) 100%),
      linear-gradient(180deg, var(--hair-dark) 0%, var(--hair-dark) 24%, var(--hair-mid) 36%, var(--skin-deep) 52%, var(--skin-mid) 72%, var(--skin-light) 90%, var(--paper) 100%);
  }
  .divider-strip {
    position: absolute; left: 278px; top: 0; width: 7px; height: 886px; background: var(--paper);
  }
  .portrait-faded {
    position: absolute; left: 285px; top: 0; width: 365px; height: 886px;
    background:
      radial-gradient(ellipse 260px 150px at 60% 5%, var(--photo-grey-1) 0%, rgba(250,250,250,0) 100%),
      radial-gradient(ellipse 220px 260px at 40% 95%, var(--photo-grey-1) 0%, rgba(250,250,250,0) 100%),
      var(--photo-grey-2);
  }
  .copy { position: absolute; left: 318px; color: var(--ink); }
  .headline {
    top: 83px; font-family: "Questrial", sans-serif; font-weight: 400; font-size: 41px; line-height: 1;
    color: var(--accent-red); letter-spacing: -0.5px;
  }
  .headline-note {
    top: 123px; font-family: "Montserrat", sans-serif; font-weight: 700; font-size: 16.5px;
  }
  .services {
    top: 170px; font-family: "Montserrat", sans-serif; font-weight: 700; font-size: 19.5px;
    line-height: 29.5px; letter-spacing: 0.2px;
  }
  .funds {
    top: 320px; font-family: "Montserrat", sans-serif; font-weight: 700; font-size: 16px;
    line-height: 24px; color: var(--accent-red);
  }
  .brand {
    position: absolute; left: 313px; top: 503px; width: 180px; height: 132px;
    display: flex; align-items: center; gap: 10px;
  }
  .brand-mark { width: 26px; height: 26px; background: var(--brand-blue); flex: none; }
  .brand-name {
    font-family: "Montserrat", sans-serif; font-weight: 700; font-size: 20px; line-height: 1.15;
    color: var(--brand-blue);
  }
  .contact { top: 647px; font-family: "Montserrat", sans-serif; font-weight: 700; font-size: 14.5px; line-height: 22.5px; }
  .contact .phone { color: var(--accent-red); font-size: 16px; }
  .about {
    top: 791px; width: 270px; font-family: "Arimo", sans-serif; font-size: 15.5px; line-height: 20px;
  }
</style>
</head>
<body>
<div class="canvas">
  <section class="advert">
    <div class="portrait-colour" role="img" aria-label="Close-up photograph of a smiling woman wearing blue-framed glasses, left half of her face"></div>
    <div class="divider-strip"></div>
    <div class="portrait-faded" role="img" aria-label="Faded greyscale photograph of the same woman with a butterfly in her hair"></div>

    <h1 class="copy headline">EYE TESTING</h1>
    <p class="copy headline-note">(SALUBRA COVERED)</p>
    <p class="copy services">PRESCRIPTION<br>GLASSES,<br>SUNGLASSES &amp;<br>CONTACT LENSES.</p>
    <p class="copy funds">ALL MAJOR<br>HEALTH FUNDS ACCEPTED.</p>

    <div class="brand">
      <span class="brand-mark"></span>
      <span class="brand-name">Larkspur<br>Vision</span>
    </div>

    <div class="copy contact">
      <p class="phone">PHONE: 95550132</p>
      <p>FOR AN APPOINTMENT AT OUR<br>CLAREMONT PRACTICE</p>
      <p class="phone">PHONE: 95550478</p>
      <p>FOR AN APPOINTMENT AT OUR<br>SUBIACO PRACTICE</p>
    </div>

    <p class="copy about">We are an independent Optometry practice providing major fashion brands in both Optical frames &amp; sunglasses.</p>
  </section>
</div>
</body>
</html>
```